Shopify store for hemp

I need a store designed for Shopify for my hemp company. I currently have a brick and mortar store, but we are looking to get some business online as well. I will upload our logo for reference. We want a clean look. Categories like THCA Flower, Concentrates, Vapes, Edibles would be nice so that we can put individual products under them. I want something about all products being third-party lab tested. All products are sourced in the United States.
Updates

Target Market(s)

Former customers who live in different areas and signed up for our marketing list.

Industry/Entity Type

Hemp/Cannabis

Coding

Coded - Design and coding required

Number of Pages Required

1 page

Requirements
Must have
• Clean feel

```html
<!DOCTYPE html>
<html lang="en">
<head>
<meta charset="utf-8">
<title>Ridgeline Hemp — Premium Hemp Products</title>
<link rel="stylesheet" href="https://fonts.googleapis.com/css2?family=Josefin+Sans:ital,wght@0,300;0,400;0,600;0,700;1,300;1,400&family=Zilla+Slab:wght@600;700&display=swap">
<style>
:root{
  --green:#1f9d55;
  --green-dark:#17814a;
  --ink:#1b1b1b;
  --muted:#6d6d6d;
  --sale:#e2a32b;
  --page:#f3f2ee;
  --card:#ffffff;
  --footer:#1e2b21;
  --line:#e6e4de;
}
*{box-sizing:border-box;margin:0;padding:0}
html,body{width:1200px;height:5319px;overflow:hidden}
body{position:relative;background:var(--page);font-family:"Josefin Sans",sans-serif;color:var(--ink)}
.abs{position:absolute}
.slab{font-family:"Zilla Slab",serif;font-weight:700;letter-spacing:3px;text-transform:uppercase}
.ph{border-radius:0}

/* top bar + header */
.topbar{top:0;left:0;width:1200px;height:29px;background:#111;color:#fff;font-size:10px;font-weight:700;letter-spacing:1px;text-align:center;line-height:31px}
.header{top:29px;left:0;width:1200px;height:82px;background:#fff}
.nav{top:48px;font-size:14px;color:#222}
.brand{top:8px;left:0;width:1200px;text-align:center}
.brand-mark{display:inline-block;width:64px;height:64px;border-radius:50%;background:var(--green);color:#fff;font-size:11px;font-weight:700;line-height:1.1;padding-top:20px;letter-spacing:.5px}
.hicon{display:inline-block;vertical-align:-3px;margin-left:6px}
.cart-badge{display:inline-block;width:28px;height:28px;border-radius:50%;background:var(--green);vertical-align:-8px;margin-left:6px;text-align:center;padding-top:6px}

/* hero */
.hero{top:105px;left:0;width:1200px;height:576px;background:linear-gradient(180deg,#cfd3c7 0%,#8c8f6e 18%,#3f5a2c 40%,#213d1c 70%,#142a12 100%)}
.hero-title{top:262px;left:0;width:1200px;text-align:center;color:#fff;font-size:52px;line-height:68px;letter-spacing:5px}
.hero-sub{top:418px;left:0;width:1200px;text-align:center;color:#fff;font-size:17px}
.btn{display:inline-block;background:var(--green);color:#fff;font-weight:700;font-size:15px;letter-spacing:.5px;text-transform:uppercase;text-align:center}
.hero-btn{top:478px;left:510px;width:180px;height:50px;line-height:54px}

/* panels */
.panel{background:#fff}
.sec-title{font-size:36px;letter-spacing:3px}
.cat-img{top:766px;width:268px;height:282px}
.cat-label{top:1071px;width:268px;text-align:center;font-family:"Zilla Slab",serif;font-weight:700;font-size:18px;letter-spacing:1px}
.dot{top:1128px;width:9px;height:9px;background:#e5e5e5}

.quality-text{font-size:12px;line-height:20px;color:#444}

/* product card */
.pcard{width:221px;height:351px;background:#fff;border:1px solid #efefef}
.pcard .tag{position:absolute;left:13px;top:10px;font-size:10px;font-weight:700;letter-spacing:1px}
.tag.sale{color:var(--sale)} .tag.new{color:var(--green)}
.pcard .img{position:absolute;left:30px;top:38px;width:160px;height:150px;border-radius:50%}
.pcard .strain{position:absolute;top:265px;width:100%;text-align:center;font-size:12px;color:#666}
.pcard .name{position:absolute;top:285px;width:100%;text-align:center;font-family:"Zilla Slab",serif;font-weight:700;font-size:13px;letter-spacing:1px;text-transform:uppercase}
.pcard .price{position:absolute;top:312px;width:100%;text-align:center;font-size:12px;color:var(--green-dark);letter-spacing:.5px}
.img.flower{background:radial-gradient(circle,#8fa64a 0%,#5f7a2f 55%,rgba(255,255,255,0) 72%)}
.img.resin{background:radial-gradient(circle,#f4b23b 0%,#d8801c 50%,rgba(255,255,255,0) 72%)}
.img.gummy{background:radial-gradient(circle at 50% 40%,#7b9051 0%,#3f7a33 50%,rgba(255,255,255,0) 72%)}
.img.preroll{background:radial-gradient(circle,#c7804f 0%,#6f9b6a 50%,rgba(255,255,255,0) 72%)}
.img.pen{background:linear-gradient(135deg,rgba(255,255,255,0) 30%,#74b9e8 42%,#a98ee0 58%,rgba(255,255,255,0) 70%)}

/* tabs */
.tab{top:3096px;height:28px;line-height:30px;border-radius:14px;background:#e4e4e2;font-size:12px;text-align:center}
.tab.active{background:#fff;color:var(--green);border:1px solid #e4e4e2}

/* reviews */
.rcard{width:382px;height:182px;background:#fff;border:1px solid #ececec;padding:22px 22px 0}
.stars{color:var(--green);font-size:16px;letter-spacing:3px}
.quote{position:absolute;right:18px;top:14px;font-family:"Zilla Slab",serif;font-size:58px;line-height:58px;color:var(--green);font-weight:700}
.rtext{margin-top:10px;font-size:12px;line-height:20px;font-style:italic;color:#444;font-weight:300}
.who{position:absolute;left:22px;bottom:20px;padding-left:40px;font-size:12px}
.avatar{position:absolute;left:0;top:0;width:32px;height:32px;border-radius:50%;background:#c9cfc6}
.who small{display:block;color:#888;font-size:10px;margin-top:3px}

/* why */
.why{top:4574px;left:0;width:1200px;height:404px;background:#f6f5f1}
.feat{top:4755px;width:240px;text-align:center}
.feat-icon{width:70px;height:70px;border-radius:50%;background:#fff;margin:0 auto 18px;display:flex;align-items:center;justify-content:center}
.feat h4{font-size:12px;font-weight:700;letter-spacing:.5px;text-transform:uppercase;margin-bottom:10px}
.feat p{font-size:10.5px;line-height:18px;color:#555}

/* footer */
.footer{top:4978px;left:0;width:1200px;height:341px;background:var(--footer);color:#fff}
.fhead{font-size:14px;font-weight:700}
.flink{font-size:12px;color:#d7dcd6;line-height:29px}
.social{width:22px;height:22px;border-radius:50%;border:1.5px solid #fff;display:inline-block;margin-right:9px}
</style>
</head>
<body>

<div class="abs topbar">WELCOME TO OUR ONLINE STORE</div>

<header class="abs header"></header>
<nav>
  <span class="abs nav" style="left:113px;top:78px">Home</span>
  <span class="abs nav" style="left:204px;top:78px">Catalog</span>
  <span class="abs nav" style="left:310px;top:78px">Collection</span>
  <span class="abs nav" style="left:427px;top:78px">Contact</span>
  <span class="abs nav" style="left:792px;top:76px">Search<svg class="hicon" width="16" height="16" viewBox="0 0 16 16"><circle cx="7" cy="7" r="5" fill="none" stroke="#222" stroke-width="1.6"/><line x1="11" y1="11" x2="15" y2="15" stroke="#222" stroke-width="1.6"/></svg></span>
  <span class="abs nav" style="left:897px;top:76px">Account<svg class="hicon" width="16" height="16" viewBox="0 0 16 16"><circle cx="8" cy="5" r="3.3" fill="none" stroke="#222" stroke-width="1.5"/><path d="M2 15c0-4 3-6 6-6s6 2 6 6" fill="none" stroke="#222" stroke-width="1.5"/></svg></span>
  <span class="abs nav" style="left:1023px;top:72px">Cart<span class="cart-badge"><svg width="16" height="16" viewBox="0 0 16 16"><path d="M1 2h2.5l2 8h7l1.5-6H5" fill="none" stroke="#fff" stroke-width="1.6"/><circle cx="6.5" cy="13.5" r="1.3" fill="#fff"/><circle cx="11.5" cy="13.5" r="1.3" fill="#fff"/></svg></span></span>
</nav>
<div class="abs brand" style="top:48px"><span class="brand-mark">RIDGELINE<br>HEMP</span></div>

<section class="abs hero" role="img" aria-label="Hemp field rows stretching toward misty mountains at sunrise"></section>
<h1 class="abs slab hero-title">Premium Hemp<br>Products</h1>
<p class="abs hero-sub">Shop THCA Flower, Concentrates, Vapes, Edibles.</p>
<a class="abs btn hero-btn">Shop Now</a>

<!-- categories -->
<section class="abs panel" style="top:634px;left:126px;width:948px;height:548px"></section>
<h2 class="abs slab sec-title" style="top:696px;left:0;width:1200px;text-align:center">Shop by Category</h2>
<div class="abs cat-img" style="left:178px;background:linear-gradient(160deg,#dfe4ea,#c9a9c4 55%,#8ea04b)" role="img" aria-label="Cup of THCA flower buds"></div>
<div class="abs cat-img" style="left:466px;background:linear-gradient(160deg,#2a1a12,#8a2a1e 50%,#c4893a)" role="img" aria-label="Concentrate bottle and boxed tincture"></div>
<div class="abs cat-img" style="left:754px;background:linear-gradient(160deg,#2b3a48,#6bbd3c 35%,#e07aa2 60%,#e9c52a)" role="img" aria-label="Colorful disposable vape pens"></div>
<div class="abs cat-label" style="left:178px">THCA FLOWER</div>
<div class="abs cat-label" style="left:466px">CONCENTRATES</div>
<div class="abs cat-label" style="left:754px">VAPES</div>
<div class="abs dot" style="left:574px"></div>
<div class="abs dot" style="left:595px;background:var(--green)"></div>
<div class="abs dot" style="left:616px"></div>

<!-- quality -->
<section class="abs panel" style="top:1222px;left:126px;width:948px;height:616px"></section>
<h2 class="abs slab" style="top:1283px;left:204px;font-size:36px;line-height:48px">Our Commitment<br>to Quality</h2>
<p class="abs quality-text" style="top:1410px;left:210px;width:380px">At <b>Ridgeline Hemp</b>, we believe in providing only the finest hemp products to our customers. Our mission is to deliver premium, lab-tested products that you can trust.</p>
<div class="abs" style="top:1280px;left:638px;width:359px;height:248px;background:linear-gradient(135deg,#3b2a16,#b7872e 40%,#5c7a3a 70%,#1f2e1a)" role="img" aria-label="Rows of tincture bottles on a shelf"></div>
<div class="abs" style="top:1518px;left:215px;width:357px;height:248px;background:linear-gradient(135deg,#8c6a3d,#d7d2c6 40%,#b6b3a8 70%,#6b5434)" role="img" aria-label="Labeled bags of hemp flower in a crate"></div>
<p class="abs quality-text" style="top:1564px;left:638px;width:365px">Every product we offer is sourced from reputable US growers who share our commitment to quality and sustainability. We work closely with independent laboratories to ensure that every batch meets our strict standards for purity, potency, and safety.</p>
<p class="abs quality-text" style="top:1690px;left:638px;width:365px">From seed to sale, we maintain complete transparency in our process. Our customers deserve to know exactly what they're getting, which is why we provide detailed lab results for all our products.</p>

<!-- best sellers -->
<h2 class="abs slab sec-title" style="top:1890px;left:130px">Best Sellers</h2>
<svg class="abs" style="top:2132px;left:76px" width="14" height="24" viewBox="0 0 14 24"><path d="M12 2L2 12l10 10" fill="none" stroke="#222" stroke-width="2"/></svg>
<svg class="abs" style="top:2132px;left:1108px" width="14" height="24" viewBox="0 0 14 24"><path d="M2 2l10 10L2 22" fill="none" stroke="#222" stroke-width="2"/></svg>

<div class="abs pcard" style="top:1968px;left:126px"><span class="tag new">NEW</span><div class="img flower" role="img" aria-label="Hemp flower bud"></div><div class="strain">Blue Dream</div><div class="name">Premium THCA Flower</div><div class="price">$110.00 – $130.00</div></div>
<div class="abs pcard" style="top:1968px;left:368px"><span class="tag sale">SALE</span><div class="img resin" role="img" aria-label="Amber live resin concentrate"></div><div class="strain">Sour Diesel</div><div class="name">Live Resin Concentrate</div><div class="price">$110.00 – $130.00</div></div>
<div class="abs pcard" style="top:1968px;left:610px"><span class="tag sale">SALE</span>
  <svg style="position:absolute;right:14px;top:10px" width="18" height="16" viewBox="0 0 18 16"><path d="M9 15S1 10 1 5a4 4 0 0 1 8-1 4 4 0 0 1 8 1c0 5-8 10-8 10z" fill="none" stroke="#222" stroke-width="1.4"/></svg>
  <svg style="position:absolute;right:15px;top:42px" width="16" height="16" viewBox="0 0 16 16"><circle cx="7" cy="7" r="5" fill="none" stroke="#222" stroke-width="1.4"/><line x1="11" y1="11" x2="15" y2="15" stroke="#222" stroke-width="1.4"/><line x1="5" y1="7" x2="9" y2="7" stroke="#222" stroke-width="1.2"/><line x1="7" y1="5" x2="7" y2="9" stroke="#222" stroke-width="1.2"/></svg>
  <div class="img pen" role="img" aria-label="Disposable vape pens"></div>
  <div class="strain" style="top:228px">Gelato</div><div class="name" style="top:248px">Disposable Vape Pen</div><div class="price" style="top:272px">$110.00 – $130.00</div>
  <a class="btn" style="position:absolute;left:36px;top:302px;width:148px;height:32px;line-height:35px;font-size:12px">Add to Cart</a></div>
<div class="abs pcard" style="top:1968px;left:852px"><span class="tag new">NEW</span><div class="img gummy" role="img" aria-label="Hemp bud on a green gummy square"></div><div class="strain">Mixed Berry</div><div class="name">Delta-8 Gummies</div><div class="price">$110.00 – $130.00</div></div>

<!-- promo -->
<div class="abs" style="top:2389px;left:130px;width:541px;height:523px;background:linear-gradient(135deg,#d8ddd2,#3f6b48 45%,#1f3a27 70%,#6a6a5e)" role="img" aria-label="Dark green tincture bottles with hemp leaves"></div>
<section class="abs" style="top:2428px;left:510px;width:564px;height:508px;background:linear-gradient(135deg,#1fa85a,#159048 60%,#1ea658)">
  <p class="abs" style="top:180px;left:50px;color:#fff;font-size:12px;letter-spacing:.5px">IT'S EASY, FAST, AND SECURE</p>
  <h2 class="abs slab" style="top:210px;left:50px;color:#fff;font-size:36px;line-height:48px">Ready to Experience<br>Premium Hemp?</h2>
  <p class="abs" style="top:322px;left:45px;color:#fff;font-size:12.5px">Discover our full collection of lab-tested, US-sourced hemp products.</p>
  <a class="abs btn" style="top:360px;left:50px;width:180px;height:50px;line-height:54px;background:#fff;color:var(--green)">Shop Now</a>
</section>

<!-- new arrivals -->
<h2 class="abs slab sec-title" style="top:3026px;left:0;width:1200px;text-align:center">New Arrivals</h2>
<span class="abs tab active" style="left:405px;width:104px">THCA Flower</span>
<span class="abs tab" style="left:530px;width:100px">Concentrates</span>
<span class="abs tab" style="left:655px;width:48px">Vapes</span>
<span class="abs tab" style="left:728px;width:58px">Edibles</span>

<div class="abs pcard" style="top:3163px;left:126px"><span class="tag sale">SALE</span><div class="img resin" role="img" aria-label="Amber live resin concentrate"></div><div class="strain">Sour Diesel</div><div class="name">Live Resin Concentrate</div><div class="price">$110.00 – $130.00</div></div>
<div class="abs pcard" style="top:3163px;left:368px"><span class="tag new">NEW</span><div class="img gummy" role="img" aria-label="Hemp bud on a green gummy square"></div><div class="strain">Mixed Berry</div><div class="name">Delta-8 Gummies</div><div class="price">$110.00 – $130.00</div></div>
<div class="abs pcard" style="top:3163px;left:610px"><span class="tag sale">SALE</span><div class="img preroll" role="img" aria-label="Colorful pre-rolls"></div><div class="strain">OG Kush</div><div class="name">THCA Pre-Rolls</div><div class="price">$110.00 – $130.00</div></div>
<div class="abs pcard" style="top:3163px;left:852px"><span class="tag new">NEW</span><div class="img flower" role="img" aria-label="Hemp flower bud"></div><div class="strain">Blue Dream</div><div class="name">Premium THCA Flower</div><div class="price">$110.00 – $130.00</div></div>

<div class="abs pcard" style="top:3534px;left:126px"><span class="tag sale">SALE</span><div class="img resin" role="img" aria-label="Amber live resin concentrate"></div><div class="strain">Sour Diesel</div><div class="name">Live Resin Concentrate</div><div class="price">$110.00 – $130.00</div></div>
<div class="abs pcard" style="top:3534px;left:368px"><span class="tag new">NEW</span><div class="img gummy" role="img" aria-label="Hemp bud on a green gummy square"></div><div class="strain">Mixed Berry</div><div class="name">Delta-8 Gummies</div><div class="price">$110.00 – $130.00</div></div>
<div class="abs pcard" style="top:3534px;left:610px"><span class="tag sale">SALE</span><div class="img preroll" role="img" aria-label="Colorful pre-rolls"></div><div class="strain">OG Kush</div><div class="name">THCA Pre-Rolls</div><div class="price">$110.00 – $130.00</div></div>
<div class="abs pcard" style="top:3534px;left:852px"><span class="tag new">NEW</span><div class="img flower" role="img" aria-label="Hemp flower bud"></div><div class="strain">Blue Dream</div><div class="name">Premium THCA Flower</div><div class="price">$110.00 – $130.00</div></div>

<!-- reviews -->
<section class="abs" style="top:3928px;left:0;width:1200px;height:646px;background:#efefec;overflow:hidden">
  <span class="abs" style="top:62px;left:128px;width:20px;height:20px;border-radius:50%;background:#d9d9d9"></span>
  <span class="abs stars" style="top:63px;left:158px;font-size:15px">★★★★★</span>
  <span class="abs" style="top:66px;left:266px;font-size:11px">256+ Five Star Reviews</span>
  <h2 class="abs slab sec-title" style="top:92px;left:126px">What Our Client Say</h2>
  <p class="abs" style="top:98px;left:805px;width:260px;font-size:12px;line-height:20px;color:#444">Join thousands of satisfied customers who trust our premium hemp products.</p>

  <div class="abs rcard" style="top:171px;left:-194px"><div class="stars">★★★★★</div><span class="quote">”</span><p class="rtext">"The quality of their THCA flower is unmatched. I love that everything is lab tested and I can see the results. Will order again!"</p><div class="who"><span class="avatar"></span>Dana Whitfield<small>Austin, TX</small></div></div>
  <div class="abs rcard" style="top:171px;left:209px"><div class="stars">★★★★★</div><span class="quote">”</span><p class="rtext">"The quality of their THCA flower is unmatched. I love that everything is lab tested and I can see the results. Will definitely be ordering again!"</p><div class="who"><span class="avatar"></span>Dana Whitfield<small>Austin, TX</small></div></div>
  <div class="abs rcard" style="top:171px;left:612px"><div class="stars">★★★★★</div><span class="quote">”</span><p class="rtext">"Fast shipping, great customer service, and premium products. The vape pens are my go-to for convenience. Highly recommend this company!"</p><div class="who"><span class="avatar"></span>Dana Whitfield<small>Austin, TX</small></div></div>
  <div class="abs rcard" style="top:171px;left:1015px"><div class="stars">★★★★★</div><span class="quote">”</span><p class="rtext">"Transparency is key for me and this company delivers. Love seeing the lab results and knowing exactly what I'm getting. Great products!"</p><div class="who"><span class="avatar"></span>Dana Whitfield<small>Austin, TX</small></div></div>

  <div class="abs rcard" style="top:386px;left:-120px"><div class="stars">★★★★★</div><span class="quote">”</span><p class="rtext">"Transparency is key for me and this company delivers. Love seeing the lab results and knowing exactly what I'm getting. Great products!"</p><div class="who"><span class="avatar"></span>Dana Whitfield<small>Austin, TX</small></div></div>
  <div class="abs rcard" style="top:386px;left:283px"><div class="stars">★★★★★</div><span class="quote">”</span><p class="rtext">"The Blue Dream strain is absolutely fantastic. You can tell they really care about quality. Plus, their prices are reasonable for such premium products."</p><div class="who"><span class="avatar"></span>Lena Alvarez<small>Austin, TX</small></div></div>
  <div class="abs rcard" style="top:386px;left:686px"><div class="stars">★★★★★</div><span class="quote">”</span><p class="rtext">"The quality of their THCA flower is unmatched. I love that everything is lab tested and I can see the results. Will definitely be ordering again!"</p><div class="who"><span class="avatar"></span>Marcus Reed<small>Austin, TX</small></div></div>
  <div class="abs rcard" style="top:386px;left:1089px"><div class="stars">★★★★★</div><span class="quote">”</span><p class="rtext">"Fast shipping, great customer service, and premium products. Highly recommend!"</p><div class="who"><span class="avatar"></span>Dana Whitfield<small>Austin, TX</small></div></div>
</section>

<!-- why choose us -->
<section class="abs why"></section>
<h2 class="abs slab sec-title" style="top:4624px;left:0;width:1200px;text-align:center">Why Choose Us</h2>
<p class="abs" style="top:4684px;left:0;width:1200px;text-align:center;font-size:12px;color:#444">Join thousands of satisfied customers who trust our premium hemp products.</p>

<div class="abs feat" style="left:106px"><div class="feat-icon"><svg width="40" height="40" viewBox="0 0 40 40" fill="none" stroke="#1f9d55" stroke-width="1.8"><rect x="9" y="6" width="20" height="27" rx="2"/><line x1="14" y1="14" x2="24" y2="14"/><line x1="14" y1="20" x2="22" y2="20"/><circle cx="27" cy="27" r="6"/><path d="M24.5 27l2 2 3.5-4"/></svg></div><h4>Lab Tested &amp; Certified</h4><p>Every product undergoes rigorous third-party lab testing to ensure purity, potency, and safety.</p></div>
<div class="abs feat" style="left:354px"><div class="feat-icon"><svg width="40" height="40" viewBox="0 0 40 40" fill="none" stroke="#1f9d55" stroke-width="1.8"><path d="M20 34V16"/><path d="M20 16c-6-1-9-6-9-10 5 1 8 5 9 10z"/><path d="M20 16c6-1 9-6 9-10-5 1-8 5-9 10z"/><path d="M8 34h24"/></svg></div><h4>100% US-Sourced Hemp</h4><p>We partner with trusted American farmers who follow strict cultivation standards.</p></div>
<div class="abs feat" style="left:606px"><div class="feat-icon"><svg width="40" height="40" viewBox="0 0 40 40" fill="none" stroke="#1f9d55" stroke-width="1.8"><path d="M6 14l14-7 14 7v14l-14 7-14-7z"/><path d="M6 14l14 7 14-7"/><line x1="20" y1="21" x2="20" y2="35"/></svg></div><h4>Fast &amp; Discreet Shipping</h4><p>Free shipping on orders over $50 with secure, discreet packaging and fast delivery.</p></div>
<div class="abs feat" style="left:856px"><div class="feat-icon"><svg width="40" height="40" viewBox="0 0 40 40" fill="none" stroke="#1f9d55" stroke-width="1.8"><rect x="9" y="18" width="8" height="16" rx="1"/><rect x="23" y="14" width="8" height="20" rx="1"/><line x1="11" y1="14" x2="15" y2="14"/><line x1="25" y1="10" x2="29" y2="10"/></svg></div><h4>Premium Quality Products</h4><p>Carefully curated selection of the finest hemp products with consistent quality.</p></div>

<!-- footer -->
<footer class="abs footer">
  <div class="abs" style="top:42px;left:128px;width:116px;height:116px;border-radius:50%;background:#fff;color:var(--green);font-weight:700;font-size:15px;text-align:center;padding-top:44px;line-height:1.2">RIDGELINE<br>HEMP</div>
  <div class="abs" style="top:184px;left:120px"><span class="social"></span><span class="social"></span><span class="social"></span><span class="social"></span></div>

  <div class="abs fhead" style="top:86px;left:440px">Quick Links</div>
  <div class="abs" style="top:110px;left:440px"><div class="flink">Shop</div><div class="flink">Categories</div><div class="flink">About</div><div class="flink">Contact</div></div>

  <div class="abs fhead" style="top:86px;left:634px">Legal</div>
  <div class="abs" style="top:110px;left:634px"><div class="flink" style="line-height:28px">Privacy Policy</div><div class="flink" style="line-height:28px">Terms of Service</div><div class="flink" style="line-height:28px">Shipping Policy</div><div class="flink" style="line-height:28px">Return Policy</div></div>

  <div class="abs fhead" style="top:88px;left:807px">Stay Updated</div>
  <p class="abs" style="top:116px;left:807px;font-size:12px;color:#d7dcd6">Subscribe to get special offers and updates.</p>
  <div class="abs" style="top:145px;left:812px;width:239px;height:44px;background:#fff;color:#666;font-size:12px;padding:16px 0 0 24px">Your Email</div>
  <a class="abs btn" style="top:203px;left:812px;width:239px;height:44px;line-height:47px;font-size:12px">Subscribe</a>

  <div class="abs" style="top:274px;left:126px;width:948px;height:1px;background:#4a564c"></div>
  <p class="abs" style="top:302px;left:438px;font-size:11px;color:#d7dcd6">Copyright © 2025 | Ridgeline Hemp</p>
</footer>

</body>
</html>
```